GownLoom.com will be an online bespoke garment creator, specifically around designing your own Wedding Dress. It will enable you to specify your own material, colours and patterns and customized features such as bows, sequins, diamantes, and more from a selection of per-defined base garments and customize them to your taste.
The concept is similar to:
www.threadwellstudio.com
But the design should reflect more like
www.velmarrow.com
www.pindle.com - (in particular the build elements)
www.korvo.com
It will be aimed at the Female marketplace. However this does not mean to use pink or portray the brand in very girly way. It should use good white space, and look very classy. not too busy, but functional and elegant, with a focus on stable and responsible site that will deliver. A wedding dress is an important purchase and to trust a company to make one for you from a distance takes a lot of trust from the customer perspective.
We want to first create the homepage and "build the dress" pages, which will consist of Enter your Measurements, Choose a Base Silhouette Style, Choose Fabric, Choose Colors, Customize Dress, Summary, Order Page, Thank you Page.
It will then have generic About us, How to Measure, Agent Locator, How it works, Contact, Order Samples, Support.
A very basic wire frame was created here to aid development, but the branding is being developed, so do not use any of it for inspiration just a visual interpretation - http://pageyard4.info/bespoke/
The link above is merely an idea on what areas the site will have. The actual design and colour scheme should reflect these sites.
The branding is also here - www.gownloom.com not the one used within that link.
The site will enable you to log in, save your designs and your delivery and measurement information. It will also offer the usual social media buttons to share the design and ability to leave comments.
This will be the first draft and the winning design will get to design the other pages and future work associated to the site.
thanks!

```html
<!DOCTYPE html>
<html lang="en">
<head>
<meta charset="utf-8">
<title>GownLoom – Choose Fabric &amp; Color</title>
<link rel="stylesheet" href="https://fonts.googleapis.com/css2?family=Sorts+Mill+Goudy&family=Arimo:wght@400;700&display=swap">
<style>
  :root{
    --ink:#111111;
    --text:#222222;
    --muted:#555555;
    --soft:#8a8a8a;
    --rule:#c9c9c9;
    --panel:#f1f1f1;
    --tab:#e6e6e6;
    --button:#e8e8e8;
    --dark:#1b1b1b;
    --white:#ffffff;
    --serif:"Sorts Mill Goudy", Georgia, serif;
    --sans:"Arimo", Arial, sans-serif;
  }
  *{box-sizing:border-box;margin:0;padding:0}
  html,body{width:1200px;height:995px;overflow:hidden;background:var(--white)}
  body{position:relative;font-family:var(--sans);color:var(--text)}
  .abs{position:absolute;white-space:nowrap}
  a{color:inherit;text-decoration:none}

  /* header */
  .flags{left:139px;top:35px;display:flex;gap:5px}
  .flag{width:14px;height:10px;border:1px solid #9aa}
  .flag.one{background:linear-gradient(#b33 0 30%,#eee 30% 60%,#34a 60%)}
  .flag.two{background:linear-gradient(#c33 0 33%,#fff 33% 66%,#24a 66%)}
  .flag.three{background:linear-gradient(90deg,#fff 40%,#c33 40% 60%,#fff 60%)}
  .brand{left:0;width:1200px;top:20px;text-align:center;font-family:var(--serif);font-size:48px;color:var(--ink);letter-spacing:-.5px}
  .account{left:897px;top:21px;font-family:var(--serif);font-size:15px;color:var(--text);display:flex}
  .account a+a{margin-left:11px;padding-left:11px;border-left:1px dotted var(--rule)}
  .search{left:872px;top:59px;width:162px;height:23px;border:1px solid #d6d6d6;border-radius:2px;background:linear-gradient(#f4f4f4,#fff);box-shadow:0 1px 2px rgba(0,0,0,.15)}
  .search svg{position:absolute;right:6px;top:4px}

  .nav{left:141px;width:921px;top:103px;height:38px;border-top:1px dotted var(--rule);border-bottom:1px dotted var(--rule)}
  .nav ul{list-style:none;position:absolute;left:0;top:0;height:100%;width:100%}
  .nav li{position:absolute;top:10px;font-family:var(--serif);font-size:14px;color:var(--ink);font-weight:700;letter-spacing:.2px;white-space:nowrap}
  .nav .active::after{content:"";position:absolute;left:-7px;right:-11px;top:24px;height:4px;background:#333}

  /* step header */
  .step-icon{left:147px;top:188px;width:42px;height:42px;border-radius:50%;background:radial-gradient(#fff 50%,#e2e2e2);box-shadow:0 3px 3px rgba(0,0,0,.12)}
  .step-title{left:194px;top:194px;font-family:var(--serif);font-size:24px;font-weight:400;color:var(--ink)}
  .pricebar{left:482px;width:580px;top:188px;height:40px;border-top:1px dotted var(--rule);border-bottom:1px dotted var(--rule);font-family:var(--serif);font-size:14px;color:var(--ink)}
  .pricebar span{position:absolute;top:11px;white-space:nowrap}
  .pricebar b{font-weight:700;letter-spacing:.3px}
  .basket-btn{left:906px;top:237px;width:155px;height:30px;background:var(--button);font-family:var(--serif);font-size:15px;color:var(--text);display:flex;align-items:center;padding-left:8px;gap:8px}
  .basket-btn .chev{margin-left:auto;margin-right:9px}

  /* tabs */
  .tabs{left:138px;top:277px;width:559px;height:49px}
  .tab{position:absolute;top:0;height:49px;border:1px solid #bdbdbd;border-bottom:none;background:linear-gradient(#f4f4f4,#e0e0e0);font-family:var(--serif);font-size:18px;color:#9a9a9a;display:flex;align-items:center;padding-left:12px;gap:9px;white-space:nowrap}
  .tab.current{background:linear-gradient(#fafafa,#f3f3f3);color:var(--ink);border:1px solid #777;border-bottom:none;z-index:2;height:50px}
  .tab-icon{flex:none;width:34px;height:34px;border-radius:50%;background:radial-gradient(#fff 50%,#dcdcdc);box-shadow:0 3px 3px rgba(0,0,0,.1);display:flex;align-items:center;justify-content:center}
  .panel{left:138px;top:325px;width:924px;height:228px;border:1px dashed #777;background:linear-gradient(#f2f2f2,#fff 45%)}

  .fabric{position:absolute;top:348px;width:160px;text-align:center;white-space:nowrap}
  .swatch-ring{margin:0 auto;width:116px;height:116px;border-radius:50%;background:radial-gradient(#fff 70%,#e0e0e0);box-shadow:0 10px 10px -6px rgba(0,0,0,.18);display:flex;align-items:center;justify-content:center}
  .swatch{width:100px;height:100px;border-radius:50%}
  .fabric h3{font-family:var(--serif);font-weight:400;font-size:17px;color:var(--ink);margin-top:12px}
  .fabric p{font-family:var(--serif);font-size:12px;color:var(--ink);margin-top:13px}
  .continue{left:879px;top:417px;width:135px;height:30px;background:var(--dark);color:#eee;font-family:var(--serif);font-size:15px;letter-spacing:.8px;display:flex;align-items:center;padding-left:13px;gap:10px}

  /* newsletter */
  .band{left:141px;width:921px;top:584px;height:83px;border-top:1px dotted var(--rule);border-bottom:1px dotted var(--rule)}
  .band-divider{left:591px;top:596px;height:58px;border-left:1px dotted #555}
  .band-title{font-family:var(--serif);font-size:12px;letter-spacing:1px;color:var(--ink);top:605px;text-align:center}
  .email{left:247px;top:626px;width:196px;height:22px;border:1px solid #ddd;font-size:12px;color:#999;padding:3px 12px}
  .go{left:443px;top:626px;width:48px;height:22px;background:linear-gradient(#f4f4f4,#dedede);border:1px solid #ddd;font-size:11px;color:#111;display:flex;align-items:center;justify-content:center;gap:3px}
  .social-btn{top:627px;height:18px;border:1px solid #ccc;border-radius:2px;background:linear-gradient(#fff,#ececec);font-size:10px;color:#333;display:flex;align-items:center;padding:0 4px;gap:3px}
  .mini-sq{width:10px;height:10px;background:#4a64a0}

  /* footer */
  .col{top:704px}
  .col h4{font-family:var(--serif);font-weight:400;font-size:15px;letter-spacing:.6px;color:var(--ink);margin-bottom:12px}
  .col ul{list-style:none}
  .col li{font-size:11px;color:var(--muted);line-height:21.9px;letter-spacing:.2px}
  .col p{font-size:11px;color:var(--muted);line-height:17.2px;width:200px;letter-spacing:.1px;white-space:normal}
  .col p a{color:var(--ink);font-weight:700;border-bottom:1px solid #333}
  .share{display:flex;gap:7px;margin-top:14px}
  .share span{width:23px;height:23px;border-radius:3px;background:linear-gradient(#9a9a9a,#6a6a6a)}

  .legal{left:141px;width:921px;top:922px;height:49px;border-top:1px dotted var(--rule);border-bottom:1px dotted var(--rule)}
  .legal nav{position:absolute;left:16px;top:16px;font-family:var(--serif);font-size:12px;font-weight:700;color:var(--ink);display:flex;gap:16px}
  .legal .copy{position:absolute;right:12px;top:17px;font-size:11px;color:var(--text)}
</style>
</head>
<body>

<header>
  <div class="abs flags" aria-label="Language">
    <span class="flag one"></span><span class="flag two"></span><span class="flag three"></span>
  </div>
  <div class="abs brand">GownLoom</div>
  <div class="abs account"><a href="#">Log in</a><a href="#">My Basket</a></div>
  <div class="abs search">
    <svg width="14" height="14" viewBox="0 0 14 14"><circle cx="5.5" cy="5.5" r="4" fill="none" stroke="#111" stroke-width="1.8"/><line x1="8.5" y1="8.5" x2="13" y2="13" stroke="#111" stroke-width="2.2"/></svg>
  </div>
  <nav class="abs nav">
    <ul>
      <li style="left:77px">Home</li>
      <li style="left:173px">About Us</li>
      <li style="left:291px">Agent Locator</li>
      <li class="active" style="left:442px">Measure Yourself</li>
      <li style="left:616px">Contact Us</li>
      <li style="left:744px">Refer a Friend</li>
    </ul>
  </nav>
</header>

<main>
  <div class="abs step-icon">
    <svg width="42" height="42" viewBox="0 0 42 42"><path d="M21 10v3M17 14h8l-2 5 3 9h-10l3-9z" fill="#1a1a1a" stroke="#1a1a1a" stroke-width="1"/><line x1="21" y1="28" x2="21" y2="33" stroke="#1a1a1a" stroke-width="1.5"/></svg>
  </div>
  <h1 class="abs step-title">Choose Fabric &amp; Color</h1>

  <div class="abs pricebar">
    <span style="left:21px"><b>Base Price:</b></span><span style="left:123px">£0</span>
    <span style="left:183px"><b>Customisations:</b></span><span style="left:316px">£0</span>
    <span style="left:377px"><b>Current Total:</b></span><span style="left:503px">£0</span>
  </div>

  <a class="abs basket-btn" href="#">
    <svg width="18" height="14" viewBox="0 0 18 14"><path d="M1 4h16l-2 9H3z" fill="#222"/><path d="M5 4l3-3M13 4l-3-3" stroke="#222" stroke-width="1.5" fill="none"/></svg>
    <span>Add to Basket</span>
    <svg class="chev" width="14" height="14" viewBox="0 0 16 16"><path d="M2 2l6 6-6 6M8 2l6 6-6 6" fill="none" stroke="#222" stroke-width="1.8"/></svg>
  </a>

  <div class="abs tabs">
    <div class="tab current" style="left:0;width:190px">
      <span class="tab-icon"><svg width="20" height="20" viewBox="0 0 20 20"><rect x="3" y="5" width="14" height="10" transform="rotate(-35 10 10)" fill="#1a1a1a"/><line x1="3" y1="15" x2="16" y2="4" stroke="#fff" stroke-width="1.2"/></svg></span>
      Choose Fabric
    </div>
    <div class="tab" style="left:190px;width:186px">
      <span class="tab-icon"><svg width="20" height="20" viewBox="0 0 20 20"><circle cx="10" cy="10" r="8" fill="none" stroke="#aaa" stroke-width="1.5"/><circle cx="8" cy="8" r="1.3" fill="#aaa"/><circle cx="12" cy="8" r="1.3" fill="#aaa"/><circle cx="8" cy="12" r="1.3" fill="#aaa"/><circle cx="12" cy="12" r="1.3" fill="#aaa"/></svg></span>
      Choose Colour
    </div>
    <div class="tab" style="left:376px;width:183px">
      <span class="tab-icon"><svg width="20" height="20" viewBox="0 0 20 20"><circle cx="11" cy="4" r="2.5" fill="#aaa"/><path d="M7 8h8v10H7z" fill="#aaa"/></svg></span>
      Choose Style
    </div>
  </div>
  <div class="abs panel"></div>

  <div class="fabric" style="left:155px">
    <div class="swatch-ring"><div class="swatch" role="img" aria-label="Orange silk fabric swatch" style="background:radial-gradient(circle at 40% 40%,#f08a5d,#d9522f 70%,#b83e20)"></div></div>
    <h3>Silk Queen</h3><p>Price: £200</p>
  </div>
  <div class="fabric" style="left:313px">
    <div class="swatch-ring"><div class="swatch" role="img" aria-label="Grey lace fabric swatch" style="background:radial-gradient(circle,#9aa0a2,#5c6364 80%)"></div></div>
    <h3>Butterfly</h3><p>Price: £250</p>
  </div>
  <div class="fabric" style="left:472px">
    <div class="swatch-ring"><div class="swatch" role="img" aria-label="Silver floral fabric swatch" style="background:radial-gradient(circle,#e4e4e4,#a9a9a9 80%)"></div></div>
    <h3>Summer flower</h3><p>Price: £150</p>
  </div>
  <div class="fabric" style="left:643px">
    <div class="swatch-ring"><div class="swatch" role="img" aria-label="Pale blue lace fabric swatch" style="background:radial-gradient(circle,#c6d6d4,#98b0ad 80%)"></div></div>
    <h3>Rosy Beauty</h3><p>Price: £300</p>
  </div>

  <a class="abs continue" href="#">CONTINUE
    <svg width="16" height="16" viewBox="0 0 16 16"><path d="M2 2l6 6-6 6M8 2l6 6-6 6" fill="none" stroke="#eee" stroke-width="1.8"/></svg>
  </a>
</main>

<section>
  <div class="abs band"></div>
  <div class="abs band-divider"></div>
  <div class="abs band-title" style="left:141px;width:450px">OUR NEWSLETTER, JOIN AND GET £10 OFF</div>
  <div class="abs email">enter email</div>
  <div class="abs go">Go <svg width="9" height="8" viewBox="0 0 9 8"><path d="M1 1l3 3-3 3M5 1l3 3-3 3" fill="none" stroke="#111" stroke-width="1.3"/></svg></div>
  <div class="abs band-title" style="left:591px;width:471px">FOLLOW US AND GET TO KNOW US BETTER</div>
  <div class="abs social-btn" style="left:752px"><b>+</b>Follow</div>
  <div class="abs social-btn" style="left:814px;color:#3b5998"><span class="mini-sq"></span>Like</div>
  <div class="abs social-btn" style="left:860px;background:#fff">14k</div>
</section>

<footer>
  <div class="abs col" style="left:157px">
    <h4>ABOUT US</h4>
    <ul><li>Our company</li><li>Our designers</li><li>Customer reviews</li><li>What the press say</li><li>Being made</li><li>Our blog</li><li>Quality &amp; environment</li></ul>
  </div>
  <div class="abs col" style="left:358px">
    <h4>HOW CAN WE HELP</h4>
    <ul><li>Contact us</li><li>FAQs</li><li>Tracking your order</li><li>Deliveries</li><li>Returns &amp; refunds</li><li>Furniture care</li><li>Gift vouchers</li></ul>
  </div>
  <div class="abs col" style="left:584px">
    <h4>JOIN US</h4>
    <ul><li>Careers</li><li>Affiliates</li></ul>
    <div class="share" aria-label="Social links"><span></span><span></span><span></span><span></span></div>
  </div>
  <div class="abs col" style="left:785px">
    <h4>OUR PRICING</h4>
    <p>Lorem ipsum dolor sit amet, consectetur adipiscing elit. Sed mattis nulla in urna dapibus pulvinar. Donec sit amet enim enim, quis convallis tellus. Nulla risus od hendrerit dui. Praesent sed iaculis massa. Suspendisse in urna ligula. Aliquam et mi sed justo convallis sagittis non vitae ligula. <a href="#">Learn more</a></p>
  </div>

  <div class="abs legal">
    <nav><a href="#">Terms &amp; conditions</a><a href="#">Privacy policy</a><a href="#">Sitemap</a></nav>
    <div class="copy">Copyright © 2012 GownLoom.com All rights reserved!</div>
  </div>
</footer>

</body>
</html>
```